Flyer to advertise gutter cleaning throughout the Autumn and winter monthss

I need a new flyer to advertise gutter and driveway cleaning, roof and gutter repairs.

I am an experienced licensed Plumber and Gasfitter looking to broaden my scope of work to gutter cleaning. I am experienced in cleaning gutter and live in a area with large gum trees. I wont something that's clear, eye catching but not too busy.

Flyer requirements: Free roof inspection - no obligation. Gutter Cleaning from $199. Pictures of men using blower or hands to clean roof gutters (no obvious faces) to be included. Australian looking houses.

A mention that 'All general plumbing maintenance' is offered as other services but not too much wording about this as the target is for gutter cleaning.

Phone number: 0437 582 316 (in this format)
Business Name: Bracken Plumbing & Gasfitting
License: 3817502
ABN: 71395046287
Web: http://brackenplumbing.example-site.net/

Target Market(s)

Elderly - busy working class

Industry/Entity Type

Plumber

Font styles to use
Sans Serif

Colors
0355a3
fbed22
ec1f27
f78f20

Requirements
Must have
• Roof Gutter Cleaning pictures
• Men in protective clothing if possible
Nice to have
• More information:
• Prevent against flooding, mold, rust, rotting and corrosion now!
• Gutter Cleaning Services
• • Remove leaves, sticks, and other debris
• • Clear away clogs
• • Test your downpipes
• • Pinpoint any gutter issues
• • Repair gutter
• With regular service, you can count on your property to be well-protected no matter what the forecast!
Should not have
• Houses that don't look Australian

```html
<!DOCTYPE html>
<html lang="en">
<head>
<meta charset="utf-8">
<title>Gutter Cleaning Flyer – Bracken Plumbing &amp; Gasfitting</title>
<link href="https://fonts.googleapis.com/css2?family=Open+Sans:ital,wght@0,400;0,600;0,700;0,800;1,600;1,700;1,800&family=Yellowtail&display=swap" rel="stylesheet">
<style>
  :root {
    --navy: #2b2766;
    --red: #e31e3c;
    --yellow: #d9cf4a;
    --teal: #137b78;
    --grey: #e3e3e3;
    --ink: #1c1c2a;
    --white: #ffffff;
    --mark: #9a9a9a;
  }
  * { margin: 0; padding: 0; box-sizing: border-box; }
  html, body { width: 924px; height: 1200px; overflow: hidden; background: var(--white); }
  body { position: relative; font-family: "Open Sans", Arial, sans-serif; }

  .crop-mark { position: absolute; background: var(--mark); }
  .crop-mark.h { height: 1px; width: 60px; }
  .crop-mark.v { width: 1px; height: 60px; }

  .flyer {
    position: absolute; left: 106px; top: 101px;
    width: 712px; height: 1001px;
    background: var(--grey); overflow: hidden;
  }
  .hero-panel {
    position: absolute; left: 0; top: 0; width: 432px; height: 421px;
    background: var(--navy);
  }
  .brand {
    position: absolute; left: 52px; top: 49px;
    display: flex; align-items: center; gap: 8px;
  }
  .brand-dot { width: 46px; height: 46px; border-radius: 50%; background: var(--red); }
  .brand-name {
    color: var(--white); font-weight: 700; font-size: 11px; line-height: 1.15;
    width: 120px; text-transform: uppercase;
  }
  .brand-rule {
    position: absolute; left: 52px; top: 133px; width: 111px; height: 3px;
    background: linear-gradient(90deg, var(--red), #f07a8a);
  }
  .headline {
    position: absolute; left: 48px; top: 150px;
    color: #f2f2f2; font-weight: 800; font-size: 67px; line-height: 72px;
    letter-spacing: 1px;
  }
  .price {
    position: absolute; left: 52px; top: 300px;
    display: flex; align-items: baseline; gap: 12px;
  }
  .price-from { font-family: "Yellowtail", cursive; color: var(--white); font-size: 52px; }
  .price-amount { color: var(--yellow); font-weight: 800; font-size: 66px; }

  .alert-band {
    position: absolute; left: 0; top: 421px; width: 432px; height: 122px;
    background: var(--red);
  }
  .alert-text {
    position: absolute; left: 52px; top: 29px; width: 300px;
    color: var(--white); font-style: italic; font-weight: 700; font-size: 19px; line-height: 27px;
  }

  .photo { position: absolute; }
  .photo-roof {
    left: 432px; top: 0; width: 280px; height: 592px;
    background: linear-gradient(170deg, #9fb0c6 0%, #56657d 45%, #6c6048 75%, #c88a2a 100%);
  }
  .photo-hands {
    left: 386px; top: 611px; width: 326px; height: 131px;
    background: linear-gradient(135deg, #d9d6cf 0%, #8a6a45 50%, #b7b2a8 100%);
  }
  .photo-gutter {
    left: 386px; top: 763px; width: 326px; height: 150px;
    background: linear-gradient(180deg, #c9cbd0 0%, #8a6f5e 35%, #7e8591 65%, #5c6270 100%);
  }
  .credential-bar {
    position: absolute; left: 386px; top: 913px; width: 326px; height: 88px;
    background: #4f5560;
    color: var(--white); font-weight: 700; font-size: 19px; line-height: 25px;
    text-align: center; padding-top: 16px;
  }

  .guarantee-seal { position: absolute; left: 331px; top: 352px; width: 202px; height: 202px; }

  .services { position: absolute; left: 37px; top: 586px; width: 340px; }
  .services-title { color: var(--navy); font-weight: 800; font-size: 22px; margin-bottom: 8px; }
  .services-list { list-style: none; }
  .services-list li {
    display: flex; align-items: center; gap: 9px;
    font-weight: 600; font-size: 15.5px; color: var(--ink); height: 26px;
  }
  .tick { width: 13px; height: 13px; flex: none; }
  .services-note {
    margin-top: 10px; font-style: italic; font-weight: 700; font-size: 11.5px; line-height: 15px; color: var(--ink);
  }

  .contact { position: absolute; left: 37px; top: 820px; width: 320px; text-align: center; }
  .offer { color: var(--navy); font-weight: 800; font-size: 21px; line-height: 26px; }
  .phone { color: var(--red); font-weight: 800; font-size: 40px; line-height: 52px; letter-spacing: 0.5px; }
  .website { color: var(--navy); font-weight: 700; font-size: 12.5px; margin-top: 2px; }
  .licence { color: #555; font-weight: 600; font-size: 11px; margin-top: 2px; }
</style>
</head>
<body>
  <span class="crop-mark v" style="left:106px;top:18px"></span>
  <span class="crop-mark v" style="left:818px;top:18px"></span>
  <span class="crop-mark v" style="left:106px;top:1122px"></span>
  <span class="crop-mark v" style="left:818px;top:1122px"></span>
  <span class="crop-mark h" style="left:20px;top:114px"></span>
  <span class="crop-mark h" style="left:844px;top:114px"></span>
  <span class="crop-mark h" style="left:20px;top:1087px"></span>
  <span class="crop-mark h" style="left:844px;top:1087px"></span>

  <main class="flyer">
    <div class="photo photo-roof" role="img" aria-label="Close-up of a tiled roof edge with autumn leaves caught in the gutter"></div>

    <section class="hero-panel">
      <div class="brand">
        <span class="brand-dot"></span>
        <span class="brand-name">Bracken Plumbing &amp; Gasfitting</span>
      </div>
      <div class="brand-rule"></div>
      <h1 class="headline">GUTTER<br>CLEANING</h1>
      <div class="price">
        <span class="price-from">From</span>
        <span class="price-amount">$199</span>
      </div>
    </section>

    <section class="alert-band">
      <p class="alert-text">Prevent against flooding, mold, rust, rotting and corrosion by CALLING US TODAY!</p>
    </section>

    <svg class="guarantee-seal" viewBox="0 0 202 202" aria-label="All work guaranteed">
      <circle cx="101" cy="101" r="99" fill="var(--white)"/>
      <circle cx="101" cy="101" r="94" fill="var(--teal)"/>
      <circle cx="101" cy="101" r="56" fill="none" stroke="var(--white)" stroke-width="4"/>
      <defs>
        <path id="seal-top" d="M 28 101 A 73 73 0 0 1 174 101"/>
        <path id="seal-bottom" d="M 22 101 A 79 79 0 0 0 180 101"/>
      </defs>
      <text fill="var(--white)" font-family="Open Sans, sans-serif" font-weight="800" font-size="24" letter-spacing="2">
        <textPath href="#seal-top" startOffset="50%" text-anchor="middle">ALL WORK</textPath>
      </text>
      <text fill="var(--white)" font-family="Open Sans, sans-serif" font-weight="800" font-size="22" letter-spacing="2">
        <textPath href="#seal-bottom" startOffset="50%" text-anchor="middle" dominant-baseline="hanging">GUARANTEED</textPath>
      </text>
      <path d="M 70 100 L 93 126 L 150 62" fill="none" stroke="var(--yellow)" stroke-width="16" stroke-linecap="round" stroke-linejoin="round"/>
    </svg>

    <section class="services">
      <h2 class="services-title">GUTTER CLEANING SERVICES</h2>
      <ul class="services-list">
        <li><svg class="tick" viewBox="0 0 12 12"><path d="M1 6.5 L4.5 10 L11 2" fill="none" stroke="var(--red)" stroke-width="1.8"/></svg>Remove leaves, sticks, and other debris</li>
        <li><svg class="tick" viewBox="0 0 12 12"><path d="M1 6.5 L4.5 10 L11 2" fill="none" stroke="var(--red)" stroke-width="1.8"/></svg>Test downpipes</li>
        <li><svg class="tick" viewBox="0 0 12 12"><path d="M1 6.5 L4.5 10 L11 2" fill="none" stroke="var(--red)" stroke-width="1.8"/></svg>Pinpoint any gutter issues</li>
        <li><svg class="tick" viewBox="0 0 12 12"><path d="M1 6.5 L4.5 10 L11 2" fill="none" stroke="var(--red)" stroke-width="1.8"/></svg>Repair gutters</li>
        <li><svg class="tick" viewBox="0 0 12 12"><path d="M1 6.5 L4.5 10 L11 2" fill="none" stroke="var(--red)" stroke-width="1.8"/></svg>New Installation</li>
      </ul>
      <p class="services-note">With regular service, you can count on your property<br>to be well-protected no matter what the forecast!</p>
    </section>

    <section class="contact">
      <p class="offer">FREE ROOF INSPECTION<br>NO OBLIGATION</p>
      <p class="phone">0437 582 316</p>
      <p class="website">brackenplumbing.example-site.net</p>
      <p class="licence">License: 3817502 | ABN: 71395046287</p>
    </section>

    <div class="photo photo-hands" role="img" aria-label="Gloved hand scooping dry leaves out of a roof gutter"></div>
    <div class="photo photo-gutter" role="img" aria-label="Roof gutter filled with leaf debris beneath a tiled roof"></div>
    <div class="credential-bar">Licensed Plumber,<br>Drainer &amp; Gasfitter</div>
  </main>
</body>
</html>
```